Consulting Practice for Charities Needs A Brochure Deisgn

Hi! We need a tri-fold brochure for a Washington, DC based consulting practice that works with charities (NGOs, Associations, etc.) and wealthy donors (philanthropists). Our company, Brennick Civic Advisors, helps nonprofits to implement practices that maximize organizational efficiency and effectiveness - by working directly with board members and staff.
Our clients are well educated and quite sophisticated (some charities are international with multi-million dollar budgets, while others are quite local and small) This brochure will be handed to them by some of our 'referral partners' (law firms, accountants and even governmental agencies) in addition to being given out during our presentations. We draw inspiration from nature and would like to somehow include a "natural / eco-friendly" feel to the piece, including natural colors .... that being said, not in any way "folksy" - it must be sophisticated.

Target Market(s)

nonprofit executive directors, board chairs, wealth holders (philanthropists)

Industry/Entity Type

Consulting

Requirements
Must have
• I uploaded a word file with content (text) - most of that needs to be on the brochure ... but ... if it looks too crowded, let me know and I'll reduce
Nice to have
• pop-out quotes (maybe from testimonials??), nature - theme of some kind but also photo of boardroom (links to samples are like are uploaded in a word doc below)
Should not have
• nothing cute ... nothing too feminine

```html
<!DOCTYPE html>
<html lang="en">
<head>
<meta charset="utf-8">
<title>Brennick Civic Advisors — Brochure Inside</title>
<link href="https://fonts.googleapis.com/css2?family=Bodoni+Moda:wght@400;500&display=swap" rel="stylesheet">
<style>
  :root{
    --ink:#000;
    --paper:#fff;
    --photo-dark:#2b2b2e;
    --photo-mid:#b9b4ae;
    --photo-light:#e9e7e4;
    --badge-teal:#1c6f8c;
    --badge-blue:#2f68b0;
    --badge-red:#c8342b;
  }
  *{margin:0;padding:0;box-sizing:border-box}
  html,body{width:1200px;height:518px;overflow:hidden;background:var(--paper)}
  body{font-family:"Bodoni Moda",serif;color:var(--ink)}
  .brochure{position:relative;width:1200px;height:518px;overflow:hidden}

  .photo{position:absolute;left:0;top:0;width:800px;height:518px;
    background:
      radial-gradient(ellipse 140px 240px at 140px 300px, #d8c3a5 0%, rgba(216,195,165,0) 100%),
      radial-gradient(ellipse 200px 300px at 640px 330px, var(--photo-dark) 0%, rgba(43,43,46,0) 100%),
      linear-gradient(90deg, var(--photo-light) 0%, var(--photo-mid) 45%, #8f8b87 70%, var(--photo-dark) 100%);}

  .box{position:absolute;display:flex;align-items:center;justify-content:center;text-align:center}
  .box.dark{background:var(--ink);color:var(--paper)}
  .box.light{background:var(--paper);color:var(--ink)}

  .heading{font-size:19px;font-weight:400;white-space:nowrap}
  .services-title{left:246px;top:0;width:153px;height:146px;align-items:flex-end;padding-bottom:17px}
  .testimonials-title{left:399px;top:64px;width:143px;height:134px;align-items:flex-end;padding-bottom:22px}

  .service{font-size:7.4px;height:20px;white-space:nowrap}
  .service-list{position:absolute;left:170px;top:210px;width:127px;height:146px;background:var(--paper);
    list-style:none;padding:28px 0 0 16px;font-size:7.2px;line-height:10.2px}
  .service-list li::before{content:"• "}

  .quote{position:absolute;font-size:7px;line-height:11.2px;padding:0 14px;display:flex;align-items:center}
  .attribution{font-size:7.2px;height:20px;white-space:nowrap}

  .back-panel{position:absolute;left:800px;top:0;width:400px;height:518px;background:var(--paper)}
  .badges{position:absolute;left:870px;top:212px;width:260px;height:56px}
  .contact{position:absolute;left:850px;top:386px;width:310px;text-align:center;font-size:7.2px;font-style:normal}
  .contact h2{font-size:11.5px;font-weight:400;margin-bottom:16px}
  .contact p{margin-bottom:13px;line-height:9.5px}
</style>
</head>
<body>
<main class="brochure">
  <div class="photo" role="img" aria-label="Boardroom photo: a businesswoman shaking hands with a colleague, staff working in a bright office behind them"></div>

  <div class="box dark services-title"><h1 class="heading">Our Services</h1></div>
  <div class="box light testimonials-title"><h2 class="heading">Testimonials</h2></div>

  <div class="box light service" style="left:118px;top:148px;width:179px">Board and Senior Staff Coaching</div>
  <div class="box dark service" style="left:118px;top:180px;width:179px">Workshops, Seminars and Retreats including</div>
  <ul class="service-list">
    <li>Roles &amp; Responsibilities</li>
    <li>Fundraising</li>
    <li>Succession Planning</li>
    <li>Board Self-Assessments</li>
    <li>Strategic Planning</li>
    <li>Board Recruitment Training</li>
    <li>Communications Development</li>
    <li>Grassroots Advocacy</li>
    <li>Mergers &amp; Acquisitions</li>
  </ul>
  <div class="box dark service" style="left:167px;top:366px;width:180px">Philanthropic Counsel</div>
  <div class="box light service" style="left:167px;top:396px;width:180px">Board Placement</div>
  <div class="box dark service" style="left:167px;top:428px;width:180px">Board Member Recruitment</div>
  <div class="box light service" style="left:167px;top:457px;width:180px">Board Retreat Planning &amp; Facilitation</div>

  <blockquote class="quote" style="left:578px;top:0;width:222px;height:156px;background:var(--ink);color:var(--paper);padding:0 22px">
    "I've had the honor and distinct privilege of working with Nora through her Board Coaching &amp; Training program. The board self-assessment process is thorough, insightful and necessary, if like me, you are challenged with finding the right organization to align with. Leveraging her expertise, guidance and deep connections throughout the Non-Profit space, Nora carefully screened several organizations as potential candidates, and went so far as to arrange introductory meetings with a select few. The entire process was educational, and an exceptional experience."
  </blockquote>
  <div class="box light attribution" style="left:572px;top:156px;width:228px;height:22px">Grant Ellery, CTFA (Client, Philanthropist)</div>

  <blockquote class="quote" style="left:651px;top:180px;width:149px;height:102px;background:var(--paper)">
    "Nora is at forefront of the new era of responsible philanthropy … Most importantly, she has the rare ability to take a vision and turn it into a coherent plan of action."
  </blockquote>
  <div class="box dark attribution" style="left:594px;top:282px;width:206px">Owen Hartley (Client, Journalist and Broadcaster)</div>

  <blockquote class="quote" style="left:446px;top:216px;width:148px;height:130px;background:var(--ink);color:var(--paper)">
    "I would recommend Nora without reservation. Her Governance Guild training and her knowledge of both Board dynamics and the needs of donors is uniquely helpful."
  </blockquote>
  <div class="box light attribution" style="left:474px;top:346px;width:216px">Miriam Colfax (CEO, Shelter Alliance of Greater DC)</div>
  <div class="box dark attribution" style="left:526px;top:369px;width:274px;height:17px">Celia Marlowe (Past Chairman, Society for Performing Arts Health)</div>

  <blockquote class="quote" style="left:560px;top:386px;width:208px;height:108px;background:var(--paper);padding:0 22px">
    "I wish you could have heard the board's comments. They were unanimously and warmly enthusiastic, saying it was the best thing we, as a board, have ever done... Thank you for the thought and combination of emotional and intellectual intelligence that you brought to the presentation."
  </blockquote>

  <section class="back-panel"></section>
  <svg class="badges" viewBox="0 0 260 56" role="img" aria-label="Certification and listing badges">
    <rect x="0" y="6" width="60" height="44" rx="4" fill="var(--badge-teal)"/>
    <circle cx="98" cy="28" r="14" fill="var(--badge-blue)"/>
    <rect x="116" y="20" width="58" height="16" fill="#222"/>
    <rect x="202" y="0" width="48" height="56" fill="var(--badge-blue)"/>
    <rect x="202" y="0" width="24" height="28" fill="var(--badge-red)"/>
  </svg>

  <address class="contact">
    <h2>Contact Us</h2>
    <p>hello@BrennickCivicAdvisors.com</p>
    <p>BrennickCivicAdvisors.com</p>
    <p>Connectline:<br>https://www.connectline.net/in/brennickcivicadvisors</p>
    <p>+1.301.555.0147</p>
  </address>
</main>
</body>
</html>
```